Design for sports training app

We need the design for 9 screens of an app that supports trainers of sport teams in preparing their training sessions. Regarding colors, fonts etc. there is absolute freedom for the designer to choose what he thinks is best.
The app will be called "Plomix", our idea for the logo is something like a stopwatch.
Wireframes are attached for every screen. You don't have to stick to those - if you have better ideas, we are happy to see them.
Our strategy is "mobile first". Based on the app design we will create a homepage later - I guess it makes sense to give this to the same person, let's see.
The deliverables are attached.
All in all the main target is to present a very simple, intuitive and nice UI that the user can work with without much learning.
Updates
Target Market(s)
Soccer trainers
Industry/Entity Type
Training
Look and feel

```html
<!DOCTYPE html>
<html lang="en">
<head>
<meta charset="utf-8">
<title>Plomix – Conditions</title>
<link href="https://fonts.googleapis.com/css2?family=Ubuntu:wght@300;400&family=Roboto:wght@400;500&display=swap" rel="stylesheet">
<style>
  :root{
    --page:#f2f2f3;
    --screen:#ffffff;
    --header-start:#275a74;
    --header-end:#10243f;
    --header-text:#ffffff;
    --label:#2e2e2e;
    --divider:#c9c9c9;
    --stepper-border:#d6d6d6;
    --stepper-sign:#8a8a8a;
    --value:#4a4a4a;
    --accent:#1f4c68;
    --accent-sign:#ffffff;
    --photo-a:#fafafa;
    --photo-b:#f1efee;
  }
  *{box-sizing:border-box;margin:0;padding:0}
  html,body{width:1200px;height:1194px;overflow:hidden;background:var(--page)}
  .canvas{position:relative;width:1200px;height:1194px}
  .screen{position:absolute;top:127px;width:530px;height:940px;background:var(--screen);overflow:hidden;box-shadow:0 2px 12px rgba(0,0,0,.08)}
  .screen--outline{left:50px}
  .screen--filled{left:620px}
  .backdrop{position:absolute;left:0;right:0;top:110px;bottom:0;
    background:radial-gradient(ellipse 45% 70% at 50% 45%,var(--photo-b) 0%,var(--photo-a) 60%,var(--screen) 100%)}
  .app-header{position:relative;height:110px;background:linear-gradient(90deg,var(--header-start),var(--header-end));color:var(--header-text)}
  .status-bar{position:absolute;top:0;left:0;right:0;height:46px;display:flex;align-items:center;justify-content:space-between;padding:0 12px;font-family:"Roboto",sans-serif;font-size:18px}
  .status-left,.status-right{display:flex;align-items:center;gap:6px;width:170px}
  .status-right{justify-content:flex-end}
  .status-time{font-weight:500}
  .nav{position:absolute;top:46px;left:0;right:0;height:64px;display:flex;align-items:center;justify-content:center}
  .nav-back{position:absolute;left:22px;top:20px}
  .nav-title{font-family:"Ubuntu",sans-serif;font-weight:400;font-size:25px;letter-spacing:-.2px}
  .conditions{position:relative;list-style:none;padding:10px 29px 0 29px}
  .condition{height:78px;display:flex;align-items:center;justify-content:space-between;border-bottom:2px dotted var(--divider)}
  .condition-label{font-family:"Ubuntu",sans-serif;font-weight:300;font-size:21px;color:var(--label);margin-top:-4px}
  .stepper{position:relative;width:120px;height:30px;margin-right:16px;margin-top:-4px;display:flex;align-items:center;justify-content:space-between}
  .stepper-btn{width:40px;height:30px;display:flex;align-items:center;justify-content:center;font-family:"Roboto",sans-serif;font-size:22px;line-height:1}
  .stepper-value{position:absolute;left:50%;top:50%;transform:translate(-50%,-50%);width:43px;height:43px;border-radius:50%;background:var(--screen);display:flex;align-items:center;justify-content:center;font-family:"Ubuntu",sans-serif;font-size:15px;color:var(--value)}
  .screen--outline .stepper{border:1.5px solid var(--stepper-border);border-radius:3px}
  .screen--outline .stepper-btn{color:var(--stepper-sign)}
  .screen--outline .stepper-value{border:1.5px solid var(--stepper-border)}
  .screen--filled .stepper{background:var(--accent);border-radius:3px;width:118px}
  .screen--filled .stepper-btn{color:var(--accent-sign);font-weight:500}
  .screen--filled .stepper-value{width:38px;height:38px;font-size:14px}
</style>
</head>
<body>
<div class="canvas">

  <section class="screen screen--outline">
    <div class="backdrop" role="img" aria-label="Faint background photo of a soccer player running"></div>
    <header class="app-header">
      <div class="status-bar">
        <div class="status-left">
          <svg width="58" height="12" viewBox="0 0 58 12"><g fill="#fff"><circle cx="6" cy="6" r="5"/><circle cx="17" cy="6" r="5"/><circle cx="28" cy="6" r="5"/></g><g fill="none" stroke="#fff" stroke-width="1.2"><circle cx="39" cy="6" r="4.4"/><circle cx="50" cy="6" r="4.4"/></g></svg>
          <span>NOVA</span>
          <svg width="20" height="14" viewBox="0 0 20 14"><g fill="none" stroke="#fff" stroke-width="2" stroke-linecap="round"><path d="M2 5a11 11 0 0 1 16 0"/><path d="M5 8.3a6.5 6.5 0 0 1 10 0"/></g><circle cx="10" cy="12" r="1.8" fill="#fff"/></svg>
        </div>
        <span class="status-time">4:21 PM</span>
        <div class="status-right">
          <svg width="10" height="18" viewBox="0 0 10 18"><path d="M1 5l8 8-4 4V1l4 4-8 8" fill="none" stroke="#fff" stroke-width="1.3"/></svg>
          <span>22%</span>
          <svg width="40" height="16" viewBox="0 0 40 16"><rect x="1" y="1" width="34" height="14" rx="2.5" fill="none" stroke="#fff" stroke-width="1.4"/><rect x="3" y="3" width="7" height="10" fill="#fff"/><rect x="36.5" y="5.5" width="2" height="5" fill="#fff"/></svg>
        </div>
      </div>
      <div class="nav">
        <svg class="nav-back" width="14" height="24" viewBox="0 0 14 24"><path d="M12 2L2 12l10 10" fill="none" stroke="#fff" stroke-width="2"/></svg>
        <h1 class="nav-title">Conditions</h1>
      </div>
    </header>
    <ul class="conditions">
      <li class="condition"><span class="condition-label">Cones</span><div class="stepper"><span class="stepper-btn">−</span><span class="stepper-value">20</span><span class="stepper-btn">+</span></div></li>
      <li class="condition"><span class="condition-label">Goals</span><div class="stepper"><span class="stepper-btn">−</span><span class="stepper-value">6</span><span class="stepper-btn">+</span></div></li>
      <li class="condition"><span class="condition-label">Players</span><div class="stepper"><span class="stepper-btn">−</span><span class="stepper-value">13</span><span class="stepper-btn">+</span></div></li>
      <li class="condition"><span class="condition-label">Goalies</span><div class="stepper"><span class="stepper-btn">−</span><span class="stepper-value">2</span><span class="stepper-btn">+</span></div></li>
    </ul>
  </section>

  <section class="screen screen--filled">
    <div class="backdrop" role="img" aria-label="Faint background photo of a soccer player running"></div>
    <header class="app-header">
      <div class="status-bar">
        <div class="status-left">
          <svg width="58" height="12" viewBox="0 0 58 12"><g fill="#fff"><circle cx="6" cy="6" r="5"/><circle cx="17" cy="6" r="5"/><circle cx="28" cy="6" r="5"/></g><g fill="none" stroke="#fff" stroke-width="1.2"><circle cx="39" cy="6" r="4.4"/><circle cx="50" cy="6" r="4.4"/></g></svg>
          <span>NOVA</span>
          <svg width="20" height="14" viewBox="0 0 20 14"><g fill="none" stroke="#fff" stroke-width="2" stroke-linecap="round"><path d="M2 5a11 11 0 0 1 16 0"/><path d="M5 8.3a6.5 6.5 0 0 1 10 0"/></g><circle cx="10" cy="12" r="1.8" fill="#fff"/></svg>
        </div>
        <span class="status-time">4:21 PM</span>
        <div class="status-right">
          <svg width="10" height="18" viewBox="0 0 10 18"><path d="M1 5l8 8-4 4V1l4 4-8 8" fill="none" stroke="#fff" stroke-width="1.3"/></svg>
          <span>22%</span>
          <svg width="40" height="16" viewBox="0 0 40 16"><rect x="1" y="1" width="34" height="14" rx="2.5" fill="none" stroke="#fff" stroke-width="1.4"/><rect x="3" y="3" width="7" height="10" fill="#fff"/><rect x="36.5" y="5.5" width="2" height="5" fill="#fff"/></svg>
        </div>
      </div>
      <div class="nav">
        <svg class="nav-back" width="14" height="24" viewBox="0 0 14 24"><path d="M12 2L2 12l10 10" fill="none" stroke="#fff" stroke-width="2"/></svg>
        <h1 class="nav-title">Conditions</h1>
      </div>
    </header>
    <ul class="conditions">
      <li class="condition"><span class="condition-label">Cones</span><div class="stepper"><span class="stepper-btn">−</span><span class="stepper-value">20</span><span class="stepper-btn">+</span></div></li>
      <li class="condition"><span class="condition-label">Goals</span><div class="stepper"><span class="stepper-btn">−</span><span class="stepper-value">6</span><span class="stepper-btn">+</span></div></li>
      <li class="condition"><span class="condition-label">Players</span><div class="stepper"><span class="stepper-btn">−</span><span class="stepper-value">13</span><span class="stepper-btn">+</span></div></li>
      <li class="condition"><span class="condition-label">Goalies</span><div class="stepper"><span class="stepper-btn">−</span><span class="stepper-value">2</span><span class="stepper-btn">+</span></div></li>
    </ul>
  </section>

</div>
</body>
</html>
```